Christmas Collection Candle Label Design

Looking to update our existing Christmas Candle Collection labels. Labels should reflect the overall feel of our brand- www.kelvabrite.ca
Want to include some color elements. Holiday colors added into design but more muted/ earthy tones not vibrant colors . Metallic elements and line art botanical illustration. Fonts should be more align to brand
Scents
Winter Lantern
Frost Berry
Amber and Fig
Belle Étoile

```html
<!DOCTYPE html>
<html lang="en">
<head>
<meta charset="utf-8">
<title>Christmas Collection Candle Labels</title>
<link rel="stylesheet" href="https://fonts.googleapis.com/css2?family=Cinzel:wght@400&family=Federo&family=Kaushan+Script&display=swap">
<style>
  :root {
    --page: #ffffff;
    --paper: #f2f0ea;
    --sage: #737a5e;
    --berry: #bf6560;
    --blush: #c99283;
    --wheat: #b9a26e;
    --band-text: #fbf8f0;
    --sage-soft: 115, 122, 94;
    --berry-soft: 191, 101, 96;
    --blush-soft: 201, 146, 131;
    --wheat-soft: 185, 162, 110;
    --gold-text: linear-gradient(90deg, #b39a5c 0%, #e6d694 30%, #d2b978 50%, #94744a 78%, #6e4e30 100%);
    --gold-band: linear-gradient(90deg, #b59b5f 0%, #d9c78c 25%, #f0e6ac 45%, #c4a870 70%, #7f5f3c 100%);
  }
  * { margin: 0; padding: 0; box-sizing: border-box; }
  html, body { width: 1200px; height: 1200px; overflow: hidden; background: var(--page); }
  .collection { position: relative; width: 1200px; height: 1200px; }

  .label {
    position: absolute; width: 442px; height: 442px;
    background: var(--paper); overflow: hidden;
  }
  .label--lantern { left: 122px; top: 120px; }
  .label--frost   { left: 644px; top: 120px; }
  .label--amber   { left: 122px; top: 645px; }
  .label--etoile  { left: 644px; top: 645px; }

  .claim-band {
    position: absolute; left: 0; top: 18px; width: 100%; height: 31px;
    display: flex; align-items: center; justify-content: center;
    font-family: "Cinzel", serif; font-size: 18.5px; color: var(--band-text);
    white-space: nowrap; z-index: 2;
  }
  .label--lantern .claim-band { background: var(--sage); }
  .label--frost   .claim-band { background: var(--berry); }
  .label--amber   .claim-band { background: var(--blush); }
  .label--etoile  .claim-band { background: var(--wheat); }

  .artwork { position: absolute; left: 0; bottom: 0; width: 100%; z-index: 0; }
  .label--lantern .artwork {
    height: 192px;
    background: linear-gradient(180deg, rgba(var(--sage-soft),0) 0%, rgba(var(--sage-soft),0.10) 30%, rgba(var(--sage-soft),0.20) 65%, rgba(var(--sage-soft),0.26) 100%);
  }
  .label--frost .artwork {
    height: 190px;
    background: linear-gradient(180deg, rgba(var(--berry-soft),0) 0%, rgba(var(--berry-soft),0.08) 35%, rgba(var(--berry-soft),0.16) 70%, rgba(var(--berry-soft),0.22) 100%);
  }
  .label--amber .artwork {
    height: 160px;
    background: linear-gradient(180deg, rgba(var(--blush-soft),0) 0%, rgba(var(--blush-soft),0.12) 30%, rgba(var(--blush-soft),0.22) 65%, rgba(var(--blush-soft),0.26) 100%);
  }
  .label--etoile .artwork {
    height: 170px;
    background: linear-gradient(180deg, rgba(var(--wheat-soft),0) 0%, rgba(var(--wheat-soft),0.12) 30%, rgba(var(--wheat-soft),0.24) 65%, rgba(var(--wheat-soft),0.30) 100%);
  }

  .scent-name {
    position: absolute; left: 0; top: 84px; width: 100%;
    text-align: center; font-weight: 400; z-index: 1;
  }
  .scent-main, .scent-accent {
    display: inline-block; background: var(--gold-text);
    -webkit-background-clip: text; background-clip: text; color: transparent;
  }
  .scent-main {
    font-family: "Federo", sans-serif; font-size: 100px; line-height: 100px;
    transform: scaleX(0.8); white-space: nowrap;
  }
  .scent-accent {
    font-family: "Kaushan Script", cursive; font-size: 66px; line-height: 70px;
    margin-top: -8px; padding: 0 8px;
  }
  .line { display: block; }

  .info-band {
    position: absolute; left: 0; top: 396px; width: 100%; height: 31px;
    background: var(--gold-band); z-index: 2;
    display: flex; align-items: center; justify-content: center; gap: 11px;
    font-family: "Cinzel", serif; color: #fdf8e8; white-space: nowrap;
  }
  .info-small { font-size: 11.5px; }
  .info-brand { font-size: 16px; }
  .info-divider { width: 1px; height: 12px; background: rgba(255,250,235,0.85); }
  .info-weight { font-size: 14.5px; }
  .info-weight small { font-size: 11.5px; }
</style>
</head>
<body>
<main class="collection">

  <section class="label label--lantern">
    <div class="claim-band">MADE WITH PLANT-BASED BOTANICALS</div>
    <div class="artwork" role="img" aria-label="Line art of pine branches and pine cones in sage green"></div>
    <h2 class="scent-name"><span class="line"><span class="scent-main">Winter</span></span><span class="line"><span class="scent-accent">Lantern</span></span></h2>
    <div class="info-band">
      <span class="info-small">MADE IN CANADA</span><span class="info-divider"></span>
      <span class="info-brand">KELVA BRITE</span><span class="info-divider"></span>
      <span class="info-weight">NET WT. <small>25 OZ | 709 G</small></span>
    </div>
  </section>

  <section class="label label--frost">
    <div class="claim-band">MADE WITH PLANT-BASED BOTANICALS</div>
    <div class="artwork" role="img" aria-label="Scattered line art snowflakes in muted berry red"></div>
    <h2 class="scent-name"><span class="line"><span class="scent-main">Frost</span></span><span class="line"><span class="scent-accent">Berry</span></span></h2>
    <div class="info-band">
      <span class="info-small">MADE IN CANADA</span><span class="info-divider"></span>
      <span class="info-brand">KELVA BRITE</span><span class="info-divider"></span>
      <span class="info-weight">NET WT. <small>25 OZ | 709 G</small></span>
    </div>
  </section>

  <section class="label label--amber">
    <div class="claim-band">MADE WITH PLANT-BASED BOTANICALS</div>
    <div class="artwork" role="img" aria-label="Line art of star anise, citrus slices and baked treats in dusty pink"></div>
    <h2 class="scent-name"><span class="line"><span class="scent-main">Amber &amp;</span></span><span class="line"><span class="scent-accent">Fig</span></span></h2>
    <div class="info-band">
      <span class="info-small">MADE IN CANADA</span><span class="info-divider"></span>
      <span class="info-brand">KELVA BRITE</span><span class="info-divider"></span>
      <span class="info-weight">NET WT. <small>25 OZ | 709 G</small></span>
    </div>
  </section>

  <section class="label label--etoile">
    <div class="claim-band">MADE WITH PLANT-BASED BOTANICALS</div>
    <div class="artwork" role="img" aria-label="Line art of poinsettias, holly and ornaments in soft gold"></div>
    <h2 class="scent-name"><span class="line"><span class="scent-main">Belle</span></span><span class="line"><span class="scent-accent">Étoile</span></span></h2>
    <div class="info-band">
      <span class="info-small">MADE IN CANADA</span><span class="info-divider"></span>
      <span class="info-brand">KELVA BRITE</span><span class="info-divider"></span>
      <span class="info-weight">NET WT. <small>25 OZ | 709 G</small></span>
    </div>
  </section>

</main>
</body>
</html>
```